Business Card Design Project

I have attached the logo and the colour pallete for the branding for the company.

Creative designs for business cards are needed.

The Company is modern corporate.

Industry/Entity Type

Business

```html
<!DOCTYPE html>
<html lang="en">
<head>
<meta charset="utf-8">
<title>Keystep Business Cards</title>
<link href="https://fonts.googleapis.com/css2?family=Open+Sans:wght@400;700&display=swap" rel="stylesheet">
<style>
  :root {
    --page-bg: #ece8e2;
    --card-white: #ffffff;
    --card-dark: #3a3b3d;
    --card-dark-edge: #2a2b2d;
    --brand-purple: #6b2a6e;
    --brand-orange: #f2a81d;
    --accent-orange: #f07a22;
    --text-grey: #4a4a4a;
    --rule-grey: #c9c9c9;
    --white: #ffffff;
  }
  * { box-sizing: border-box; margin: 0; padding: 0; }
  html, body {
    width: 1200px; height: 1023px; overflow: hidden;
    background: var(--page-bg);
    font-family: "Open Sans", Arial, sans-serif;
  }
  .card {
    position: absolute;
    width: 560px; height: 320px;
    border-radius: 3px;
    box-shadow: 0 6px 18px rgba(0,0,0,.18);
    overflow: hidden;
  }
  .card-front { left: 90px; top: 120px; background: var(--card-white); }
  .card-back {
    left: 550px; top: 580px;
    background: linear-gradient(150deg, #4a4b4e 0%, var(--card-dark) 45%, var(--card-dark-edge) 100%);
  }
  .wordmark {
    position: absolute;
    font-weight: 700;
    letter-spacing: -2px;
    line-height: 1;
  }
  .card-front .wordmark { left: 34px; top: 70px; font-size: 92px; color: var(--brand-purple); }
  .card-back .wordmark { left: 0; right: 0; top: 108px; text-align: center; font-size: 96px; color: var(--white); }
  .corner-tab {
    position: absolute; background: var(--brand-orange);
  }
  .card-front .corner-tab { right: 0; top: 0; width: 60px; height: 12px; }
  .card-back .corner-tab { left: 0; bottom: 56px; width: 12px; height: 44px; }
  .holder { position: absolute; left: 40px; top: 196px; }
  .holder-name { font-size: 26px; font-weight: 700; color: var(--brand-purple); }
  .holder-role { font-size: 15px; color: var(--text-grey); margin-top: 2px; }
  .contact {
    position: absolute; left: 340px; top: 196px;
    padding-left: 14px; border-left: 1px solid var(--rule-grey);
    font-size: 12.5px; line-height: 1.45; color: var(--text-grey);
  }
  .contact b { color: var(--accent-orange); font-weight: 700; display: inline-block; width: 16px; }
  .website {
    position: absolute; right: 40px; top: 232px;
    font-size: 16px; color: #d9d9d9; letter-spacing: .5px;
  }
</style>
</head>
<body>
  <section class="card card-front">
    <span class="corner-tab"></span>
    <div class="wordmark">keystep</div>
    <div class="holder">
      <div class="holder-name">Your Nameee</div>
      <div class="holder-role">Manging Director</div>
    </div>
    <div class="contact">
      <div><b>P:</b>XXX-XXX-XXXX</div>
      <div><b>F:</b>XXX-XXX-XXXX</div>
      <div><b>E:</b>info@keystep.com</div>
      <div>Your Local Address number</div>
      <div>Goes here</div>
    </div>
  </section>

  <section class="card card-back">
    <span class="corner-tab"></span>
    <div class="wordmark">keystep</div>
    <div class="website">www.keystep.com</div>
  </section>
</body>
</html>
```